Copper Ridge Athletics Web Design

Need to completely update website - simple and clean look - informative
this will be our main source for booking appointments etc. needs to have baseball and softball content. we currently have a site - looking to update - we would like you to design and add to our current site.

Target Market(s)

ages 15-45, youth and parents for kids- softball and baseball players /fitness

Industry/Entity Type

baseball and softball indoor training facility

Coding

Coded - Design and coding required

Number of Pages Required

5+ page

Colors

Designer to choose colors to be used in the design.

Requirements
Must have
• our colors of business are green and black- we need you to completely set up the website for us
Nice to have
• out current webiste is www.copperridge482.example

```html
<!DOCTYPE html>
<html lang="en">
<head>
<meta charset="utf-8">
<title>Copper Ridge Athletics</title>
<link href="https://fonts.googleapis.com/css2?family=Teko:wght@500;600&family=Roboto:wght@400;700&family=Yellowtail&display=swap" rel="stylesheet">
<style>
:root{
  --green:#3df019;
  --dark:#1f2124;
  --white:#ffffff;
  --text:#666a70;
  --accent:#e8453c;
  --turf-top:#4a5a3c;
  --turf-bottom:#6f9a4a;
}
*{margin:0;padding:0;box-sizing:border-box}
html,body{width:1200px;height:959px;overflow:hidden;background:var(--white);font-family:'Roboto',sans-serif}
.hero{position:relative;width:1200px;height:516px;background:linear-gradient(180deg,#2b2f2a 0%,#3c4a36 35%,var(--turf-top) 55%,var(--turf-bottom) 100%)}
.site-header{position:absolute;top:0;left:0;width:1200px;height:63px;border-bottom:1px solid rgba(255,255,255,.18);display:flex;align-items:center}
.brand{margin-left:37px;display:flex;align-items:center;gap:7px;font-family:'Teko',sans-serif;font-weight:600;font-size:22px;color:var(--white);letter-spacing:.5px;width:186px}
.brand-mark{width:10px;height:10px;background:var(--green);border-radius:50%}
.main-nav{display:flex;gap:20px;margin-left:16px;font-family:'Teko',sans-serif;font-weight:500;font-size:13.5px;color:var(--white);letter-spacing:.2px}
.main-nav .active{color:var(--green)}
.main-nav .has-sub::after{content:"⌄";font-size:9px;margin-left:2px}
.header-tools{display:flex;gap:12px;align-items:center;margin-left:88px}
.social-dot{width:8px;height:8px;border-radius:50%;background:var(--white)}
.header-contact{position:absolute;right:0;top:0;height:63px;width:202px;border-left:1px solid rgba(255,255,255,.18);display:flex;align-items:center;padding-left:24px;gap:10px}
.header-contact .label{font-family:'Teko',sans-serif;font-weight:600;font-size:15px;color:var(--white);line-height:1}
.header-contact .phone{font-size:10px;color:var(--white);margin-top:4px}
.hero-copy{position:absolute;left:222px;top:193px}
.hero-bar{position:absolute;left:191px;top:197px;width:5px;height:134px;background:var(--green)}
.hero-bar-small{position:absolute;left:172px;top:302px;width:5px;height:29px;background:var(--white)}
.hero-kicker{font-family:'Yellowtail',cursive;font-size:22px;color:var(--green)}
.hero-title{font-family:'Teko',sans-serif;font-weight:600;font-size:52px;line-height:.98;color:var(--white);margin-top:4px}
.btn{display:inline-block;font-family:'Roboto',sans-serif;font-weight:700;font-size:9px;letter-spacing:.3px;text-transform:uppercase}
.btn-green{background:var(--green);color:var(--white)}
.hero .btn-green{margin-top:16px;padding:9px 19px}
.about{position:absolute;top:572px;left:225px;width:760px}
.about-media{position:absolute;left:0;top:0;width:347px;height:350px;background:linear-gradient(160deg,#6e6b60 0%,#3a3b3e 45%,#8a6f5a 100%)}
.play{position:absolute;left:325px;top:131px}
.about-copy{position:absolute;left:406px;top:23px;width:350px}
.eyebrow{font-size:8.5px;color:var(--accent);text-transform:uppercase;letter-spacing:.3px}
.about-title{font-family:'Teko',sans-serif;font-weight:600;font-size:33px;line-height:1.05;color:var(--dark);margin-top:6px}
.about-text{font-size:8.4px;line-height:15px;color:var(--text);margin-top:14px}
.points{list-style:none;margin-top:18px}
.points li{font-size:8.4px;color:var(--text);height:18px;display:flex;align-items:center;gap:9px}
.actions{display:flex;gap:9px;margin-top:20px}
.actions .btn{height:31px;display:flex;align-items:center;padding:0 19px}
.btn-outline{border:1px solid var(--dark);color:var(--dark)}
</style>
</head>
<body>
<section class="hero">
  <div role="img" aria-label="Indoor batting cages and turf field with players training" style="position:absolute;inset:0"></div>
  <header class="site-header">
    <div class="brand"><span class="brand-mark"></span>Copper Ridge Athletics</div>
    <nav class="main-nav">
      <span class="active has-sub">HOME</span><span class="has-sub">ABOUT US</span><span class="has-sub">LESSONS</span><span class="has-sub">TEAM RENTAL PRICING</span><span class="has-sub">INSTRUCTOR OPPORTUNITIES</span><span>CAMPS/CLASSES</span><span>CONTACT US</span>
    </nav>
    <div class="header-tools">
      <svg width="11" height="11" viewBox="0 0 11 11"><circle cx="4.5" cy="4.5" r="3.5" fill="none" stroke="#fff" stroke-width="1.4"/><line x1="7" y1="7" x2="10" y2="10" stroke="#fff" stroke-width="1.4"/></svg>
      <span class="social-dot"></span><span class="social-dot"></span><span class="social-dot"></span><span class="social-dot"></span><span class="social-dot"></span>
    </div>
    <div class="header-contact">
      <svg width="28" height="22" viewBox="0 0 28 22"><ellipse cx="12" cy="9" rx="11" ry="8" fill="#3df019"/><path d="M5 15 L3 21 L10 16Z" fill="#3df019"/><ellipse cx="18" cy="13" rx="9" ry="6" fill="#2fc412"/></svg>
      <div><div class="label">Have Any Questions</div><div class="phone">+ 1 555-014-8260</div></div>
    </div>
  </header>
  <div class="hero-bar"></div><div class="hero-bar-small"></div>
  <div class="hero-copy">
    <div class="hero-kicker">Welcome to Copper Ridge!</div>
    <h1 class="hero-title">Baseball and Softball<br>Training Facility</h1>
    <a class="btn btn-green">Get Started</a>
  </div>
</section>
<section class="about">
  <div class="about-media" role="img" aria-label="Young catchers in gear practising in the training facility"></div>
  <svg class="play" width="58" height="58" viewBox="0 0 58 58"><circle cx="29" cy="29" r="28" fill="#3df019" opacity=".3"/><circle cx="29" cy="29" r="21" fill="#3df019"/><path d="M25 22 L36 29 L25 36Z" fill="#fff"/></svg>
  <div class="about-copy">
    <div class="eyebrow">About Us</div>
    <h2 class="about-title">Hitting, Pitching, Fielding<br>and More</h2>
    <p class="about-text">Lorem lipsum amet set dc'core as livasta, after you decide to start training we will make sure you get the best fitness program. Our sport experts and latest sports equipment are the winning combination of gym exercises.</p>
    <ul class="points">
      <li><svg width="10" height="6" viewBox="0 0 10 6"><path d="M0 3H9M6 0.5L9 3L6 5.5" stroke="#3df019" fill="none"/></svg>2,000+ locations open (and we're just getting started!)</li>
      <li><svg width="10" height="6" viewBox="0 0 10 6"><path d="M0 3H9M6 0.5L9 3L6 5.5" stroke="#3df019" fill="none"/></svg>Unique concept that combines fitness and technology</li>
      <li><svg width="10" height="6" viewBox="0 0 10 6"><path d="M0 3H9M6 0.5L9 3L6 5.5" stroke="#3df019" fill="none"/></svg>We have small studios designed for the large groups</li>
      <li><svg width="10" height="6" viewBox="0 0 10 6"><path d="M0 3H9M6 0.5L9 3L6 5.5" stroke="#3df019" fill="none"/></svg>1800+ franchises awarded in 30 countries worldwide</li>
    </ul>
    <div class="actions"><a class="btn btn-green">Read More</a><a class="btn btn-outline">Contact Us</a></div>
  </div>
</section>
</body>
</html>
```